MotoBrisk flyer design

I need something that is bold and punchy for a new mobile vehicle valet based in Telford, Shropshire with own water and electricity supply. I have aimed for all colours to be blue and yellow and the flyer must show a special summer offer of "FREE TYRE PRESSURE CHECK AND ADJUSTMENT IF REQUIRED WITH EVERY VALET". I aim to make this business as professionally run as possible and the flyers should echo that.

Requirements
Must have
• Company name - MotoBrisk
Slogan - Where perfection is the only option
Special offer - FREE TYRE PRESSURE CHECK AND ADJUSTMENT WITH EVERY VALET.
Image - vehicle being washed
All contact details - www.motobrisk-demo.co.uk
sales@motobrisk-demo.co.uk
07700900318

```html
<!DOCTYPE html>
<html lang="en">
<head>
<meta charset="utf-8">
<title>MotoBrisk flyer</title>
<link rel="stylesheet" href="https://fonts.googleapis.com/css2?family=Arimo:wght@400;700&family=Roboto+Condensed:wght@700&display=swap">
<style>
  :root {
    --backdrop: #021a08;
    --frame-top: #dc6f30;
    --frame-bottom: #e9ae31;
    --panel-top: #ffffff;
    --panel-bottom: #c9c9cd;
    --brand-green: #5aad4e;
    --slogan-grey: #666666;
    --contact-blue: #2a74c2;
    --burst-red: #d02a2a;
    --burst-text: #ffe23a;
    --photo-border: #ffffff;
  }
  html, body {
    margin: 0;
    width: 1200px;
    height: 1200px;
    overflow: hidden;
    background: var(--backdrop);
  }
  .canvas {
    position: relative;
    width: 1200px;
    height: 1200px;
  }
  .flyer-frame {
    position: absolute;
    left: 252px;
    top: 151px;
    width: 695px;
    height: 896px;
    background: linear-gradient(to bottom, var(--frame-top), var(--frame-bottom) 70%);
  }
  .flyer-panel {
    position: absolute;
    left: 44px;
    top: 48px;
    width: 606px;
    height: 798px;
    background: linear-gradient(to bottom, var(--panel-top) 62%, var(--panel-bottom));
    overflow: hidden;
  }
  .brand-name {
    position: absolute;
    top: 28px;
    left: 0;
    width: 100%;
    margin: 0;
    text-align: center;
    font-family: "Arimo", Arial, sans-serif;
    font-weight: 700;
    font-size: 108px;
    line-height: 1;
    letter-spacing: -1px;
    color: var(--brand-green);
  }
  .slogan {
    position: absolute;
    top: 130px;
    left: 0;
    width: 100%;
    margin: 0;
    text-align: center;
    font-family: "Arimo", Arial, sans-serif;
    font-weight: 700;
    font-size: 33px;
    color: var(--slogan-grey);
  }
  .photo {
    position: absolute;
    border: 7px solid var(--photo-border);
    box-shadow: 2px 4px 8px rgba(0,0,0,0.35);
  }
  .photo-bonnet {
    left: 155px;
    top: 183px;
    width: 372px;
    height: 245px;
    transform: rotate(2deg);
    background:
      radial-gradient(ellipse at 70% 20%, rgba(255,255,255,0.55), transparent 35%),
      linear-gradient(160deg, #3e63b8 0%, #1b3b8e 45%, #0b1c58 100%);
  }
  .photo-windscreen {
    left: 24px;
    top: 377px;
    width: 392px;
    height: 242px;
    transform: rotate(-2.5deg);
    background:
      radial-gradient(ellipse at 40% 35%, rgba(230,240,250,0.7), transparent 45%),
      linear-gradient(to bottom, #7aa6cf 0%, #3f73ac 60%, #1c2c44 100%);
  }
  .offer-burst {
    position: absolute;
    left: 374px;
    top: 430px;
    width: 214px;
    height: 214px;
  }
  .offer-text {
    position: absolute;
    left: 0;
    top: 0;
    width: 214px;
    height: 214px;
    display: flex;
    flex-direction: column;
    justify-content: center;
    align-items: center;
    margin: 0;
    font-family: "Roboto Condensed", "Arial Narrow", sans-serif;
    font-weight: 700;
    font-size: 14px;
    line-height: 1.15;
    text-align: center;
    color: var(--burst-text);
    transform: rotate(-14deg);
  }
  .contact-line {
    position: absolute;
    top: 672px;
    left: 0;
    width: 100%;
    margin: 0;
    text-align: center;
    font-family: "Arimo", Arial, sans-serif;
    font-size: 23px;
    color: var(--contact-blue);
  }
  .phone-number {
    position: absolute;
    top: 690px;
    left: 0;
    width: 100%;
    margin: 0;
    text-align: center;
    font-family: "Arimo", Arial, sans-serif;
    font-weight: 700;
    font-size: 92px;
    letter-spacing: -2px;
    color: var(--contact-blue);
  }
</style>
</head>
<body>
<div class="canvas">
  <div class="flyer-frame">
    <div class="flyer-panel">
      <h1 class="brand-name">MotoBrisk</h1>
      <p class="slogan">Where perfection is the only option</p>

      <div class="photo photo-bonnet" role="img" aria-label="Photo of a hand washing a dark blue car bonnet with a soapy sponge"></div>
      <div class="photo photo-windscreen" role="img" aria-label="Photo of a hose spraying water onto a car windscreen"></div>

      <div class="offer-burst">
        <svg width="214" height="214" viewBox="-107 -107 214 214" aria-hidden="true">
          <g fill="var(--burst-red)">
            <rect x="-76" y="-76" width="152" height="152" transform="rotate(0)"/>
            <rect x="-76" y="-76" width="152" height="152" transform="rotate(15)"/>
            <rect x="-76" y="-76" width="152" height="152" transform="rotate(30)"/>
            <rect x="-76" y="-76" width="152" height="152" transform="rotate(45)"/>
            <rect x="-76" y="-76" width="152" height="152" transform="rotate(60)"/>
            <rect x="-76" y="-76" width="152" height="152" transform="rotate(75)"/>
          </g>
        </svg>
        <p class="offer-text">
          <span>SPECIAL OFFER</span>
          <span>FREE TYRE PRESSURE</span>
          <span>CHECK AND ADJUSTMENT</span>
          <span>WITH EVERY VALET.</span>
        </p>
      </div>

      <p class="contact-line">www.motobrisk-demo.co.uk &bull; sales@motobrisk-demo.co.uk</p>
      <p class="phone-number">07700900318</p>
    </div>
  </div>
</div>
</body>
</html>
```